Online trading school - Website design

We are building an online trading school (trading of shares, commodities, indices, currencies). The purpose is to teach online traders how to trade successfully. We need to design the homepage of the website and logo (bramwelloq.com will be the domain). The homepage will contain the following elements

- logo
- Sign in and Register links/buttons
- upper menu
- short introduction
- a couple of bullet points 'Why to join our school?'
- sign up form
- text
- bottom menu

Attached is a draft for the designer. The draft is just for an inspiration, the actual structure of the website can be different if the designer thinks so.

The designer is free to choose colors.

School

3 page

```html
<!DOCTYPE html>
<html lang="en">
<head>
<meta charset="utf-8">
<title>Online Trading School</title>
<link href="https://fonts.googleapis.com/css2?family=Roboto:wght@400;500&family=Open+Sans:wght@400;600&display=swap" rel="stylesheet">
<style>
:root{
  --blue:#0b66b1;
  --blue-dark:#0a5a9c;
  --yellow:#fbb200;
  --ink:#333;
  --muted:#555;
  --light:#f4f4f4;
  --nav:#f7f7f7;
  --footer:#222;
  --white:#fff;
}
*{box-sizing:border-box;margin:0;padding:0}
html,body{width:1200px;height:977px;overflow:hidden}
body{position:relative;background:var(--white);font-family:"Roboto",sans-serif;color:var(--ink)}
.abs{position:absolute}

.site-header{left:0;top:0;width:1200px;height:60px;background:#efefef}
.brand{left:111px;top:12px;font-family:"Roboto",sans-serif;font-weight:500;font-size:25px;line-height:36px;color:var(--blue);letter-spacing:-.2px}
.btn-head{top:13px;height:34px;border-radius:3px;color:var(--white);font:500 15px/34px "Roboto",sans-serif;display:flex;align-items:center;gap:7px;padding-left:12px}
.btn-signin{left:844px;width:103px;background:var(--yellow)}
.btn-register{left:956px;width:133px;background:var(--blue);padding-left:20px}

.main-nav{left:0;top:60px;width:1200px;height:41px;background:var(--nav)}
.main-nav ul{list-style:none;position:absolute;left:111px;top:0;display:flex;height:41px}
.main-nav li{font-size:15px;line-height:41px;color:#555;padding:0 16px}
.main-nav li.active{background:var(--blue);color:var(--white);padding:0 7px;margin-right:14px}
.social-head{top:68px;display:flex;gap:8px;left:989px}
.social-head span{width:27px;height:27px;border-radius:50%}

.hero{left:0;top:101px;width:1200px;height:343px;overflow:hidden}
.hero-photo{left:0;top:0;width:1200px;height:343px;background:linear-gradient(100deg,#dfe6ea 40%,#b9c4cc 60%,#c98b6a 85%,#e1d6cc)}
.hero-title{left:128px;top:34px;font-size:43px;line-height:50px;font-weight:500;color:var(--blue);letter-spacing:-.5px}
.rule{height:5px;width:84px;background:var(--white)}
.benefits{left:128px;top:126px;list-style:none}
.benefits li{display:flex;align-items:center;gap:10px;font-size:18.5px;font-weight:500;color:#3a3a3a;height:32px}

.join-card{left:589px;top:32px;width:499px;height:283px;background:rgba(11,102,177,.93);padding:0 29px}
.join-title{margin-top:2px;font-size:44px;font-weight:500;color:var(--white);letter-spacing:-.5px;line-height:60px}
.join-card .rule{background:var(--yellow);margin-top:3px}
.field{display:block;width:440px;height:46px;background:var(--white);border:0;border-radius:3px;margin-top:6px;padding-left:16px;font:400 15px "Roboto",sans-serif;color:#333}
.field:first-of-type{margin-top:14px}
.agree{left:29px;top:252px;display:flex;align-items:center;gap:7px;color:var(--white);font-size:13.5px;letter-spacing:-.2px}
.agree i{width:14px;height:14px;background:var(--white);border-radius:2px}
.btn-submit{left:349px;top:234px;width:120px;height:38px;background:var(--yellow);border-radius:3px;color:var(--white);font:500 15px/38px "Roboto",sans-serif;text-align:center}

.offer{left:0;top:444px;width:1200px;height:329px;background:var(--light)}
.offer-photo{left:0;top:0;width:550px;height:329px;background:linear-gradient(120deg,#e6ece6,#a6aeb2 45%,#7a6a60 75%,#c7a48c)}
.offer-title{left:575px;top:22px;font-size:43px;font-weight:500;color:var(--blue);letter-spacing:-.5px}
.offer .rule{left:575px;top:79px;background:var(--yellow)}
.offer-text{left:575px;top:105px;width:515px;font:400 14.6px/19px "Open Sans",sans-serif;color:var(--muted)}
.offer-text p+p{margin-top:19px}

.site-footer{left:0;top:773px;width:1200px;height:127px;background:var(--footer);color:var(--white)}
.foot-h{top:15px;font-size:19px;font-weight:400}
.social-foot{left:114px;top:50px;display:flex;gap:8px}
.social-foot span{width:28px;height:28px;border-radius:50%;background:var(--white)}
.newsletter{left:380px;top:55px;display:flex}
.newsletter .email{width:262px;height:40px;background:var(--white);padding-left:18px;font:400 15px/40px "Roboto",sans-serif;color:#777}
.newsletter .btn-signup{width:86px;height:40px;background:var(--yellow);font:500 15px/40px "Roboto",sans-serif;text-align:center}
.news{left:805px;top:54px;font:400 18px/21px "Open Sans",sans-serif}
.notch{left:578px;top:112px}

.legal{left:0;top:900px;width:1200px;height:77px;background:var(--blue);color:var(--white);font:600 11.5px/1 "Open Sans",sans-serif}
.legal .links{left:111px;top:31px}
.legal .copy{right:111px;top:31px}
</style>
</head>
<body>

<header class="abs site-header">
  <div class="abs brand">ONLINE TRADING SCHOOL</div>
  <div class="abs btn-head btn-signin">
    <svg width="20" height="20" viewBox="0 0 20 20" fill="none" stroke="#fff" stroke-width="1.6"><rect x="2" y="2" width="16" height="16" rx="2"/><path d="M6 10h8M11 7l3 3-3 3"/></svg>SIGN IN
  </div>
  <div class="abs btn-head btn-register">
    <svg width="20" height="20" viewBox="0 0 20 20" fill="none" stroke="#fff" stroke-width="1.6"><rect x="2" y="2" width="16" height="16" rx="2"/><path d="M5 6h1M8 6h7M5 10h1M8 10h7M5 14h1M8 14h7"/></svg>REGISTER
  </div>
</header>

<nav class="abs main-nav">
  <ul>
    <li class="active">About Our School</li>
    <li>Risk Warning</li>
    <li>FAQ</li>
    <li>Trading Glossary</li>
    <li>Contact</li>
  </ul>
</nav>
<div class="abs social-head">
  <span style="background:#2f5b9a"></span>
  <span style="background:#29a9e1"></span>
  <span style="background:#dd4b39"></span>
</div>

<section class="abs hero">
  <div class="abs hero-photo" role="img" aria-label="Photo of a trading instructor working with students at desks"></div>
  <svg class="abs" style="left:0;top:0" width="1200" height="343">
    <polygon points="0,0 564,0 448,172 587,343 0,343" fill="#fbb200"/>
    <polyline points="564,0 448,172 587,343" fill="none" stroke="#fff" stroke-width="8"/>
  </svg>
  <h1 class="abs hero-title">Why to join us?</h1>
  <div class="abs rule" style="left:128px;top:93px"></div>
  <ul class="abs benefits">
    <li><svg width="20" height="20" viewBox="0 0 20 20"><circle cx="10" cy="10" r="9" fill="#5aa524"/><path d="M5.5 10.5l3 3 6-6" fill="none" stroke="#fff" stroke-width="2"/></svg>Best trading tips ever</li>
    <li><svg width="20" height="20" viewBox="0 0 20 20"><circle cx="10" cy="10" r="9" fill="#5aa524"/><path d="M5.5 10.5l3 3 6-6" fill="none" stroke="#fff" stroke-width="2"/></svg>Secret tips from experts</li>
    <li><svg width="20" height="20" viewBox="0 0 20 20"><circle cx="10" cy="10" r="9" fill="#5aa524"/><path d="M5.5 10.5l3 3 6-6" fill="none" stroke="#fff" stroke-width="2"/></svg>We teach you how to trade online</li>
    <li><svg width="20" height="20" viewBox="0 0 20 20"><circle cx="10" cy="10" r="9" fill="#5aa524"/><path d="M5.5 10.5l3 3 6-6" fill="none" stroke="#fff" stroke-width="2"/></svg>Learn how to trade commodities</li>
    <li><svg width="20" height="20" viewBox="0 0 20 20"><circle cx="10" cy="10" r="9" fill="#5aa524"/><path d="M5.5 10.5l3 3 6-6" fill="none" stroke="#fff" stroke-width="2"/></svg>Learn how to become a trader</li>
  </ul>

  <form class="abs join-card">
    <h2 class="join-title">Join our school now!</h2>
    <div class="rule"></div>
    <input class="field" placeholder="First Name">
    <input class="field" placeholder="Last Name">
    <input class="field" placeholder="Email">
    <div class="abs agree"><i></i>Agree with our terms and conditions</div>
    <div class="abs btn-submit">SUBMIT</div>
  </form>
</section>

<section class="abs offer">
  <div class="abs offer-photo" role="img" aria-label="Photo of students working at computers in a classroom"></div>
  <h2 class="abs offer-title">What do we offer?</h2>
  <div class="abs rule"></div>
  <div class="abs offer-text">
    <p>Lorem ipsum dolor sit amet, consectetuer adipiscing elit, sed diam nonummy nibh euismod tincidunt ut laoreet dolore magna aliquam erat volutpat. Ut wisi enim ad minim veniam, quis nostrud exerci tation ullamcorper suscipit lobortis nisl ut aliquip ex ea commodo consequat.</p>
    <p>Duis autem vel eum iriure dolor in hendrerit in vulputate velit esse molestie cnsequat, vel illum dolore eu feugiat nulla facilisis at vero eros et accumsan et iusto odio dignissim qui blandit praesent luptatum zzril delenit augue duis dolore te feugait nulla facilisi. Nam liber tempor cum soluta nobis eleifend option congue nihil imperdiet doming..</p>
  </div>
</section>

<footer class="abs site-footer">
  <h3 class="abs foot-h" style="left:114px">Follow us on Social Media</h3>
  <div class="abs social-foot"><span></span><span></span><span></span></div>
  <h3 class="abs foot-h" style="left:379px">Sign up and have exclusive offers</h3>
  <div class="abs newsletter"><div class="email">Email..</div><div class="btn-signup">SIGN UP</div></div>
  <h3 class="abs foot-h" style="left:805px">Latest News</h3>
  <p class="abs news">Lorem ipsum dolor sit amet, cmassa.<br>Cum sociis natoque</p>
  <svg class="abs notch" width="40" height="15"><polygon points="0,15 20,0 40,15" fill="#0b66b1"/></svg>
</footer>

<div class="abs legal">
  <span class="abs links">TERMS AND CONDITIONS - PRIVACY PROTECTION</span>
  <span class="abs copy">© 2016 Online trading school -&nbsp; All Rights Reserved</span>
</div>

</body>
</html>
```